4x6 Postcard Design Full Color Double Sided

Hello, I am in need of a postcard design. The document with details is attached. And I am writing here also:

To My Dear Colleague,

This week, I want you to do yourself and me a favor, okay?

I want you to ask your boss for a $100,000 per year salary increase. If the answer is no then I want you to “give yourself” a

$10,000 per month pay increase RIGHT NOW!

The opportunity to make 6-7 figures using SIMPLE online systems is exploding right before your eyes. Why aren’t you paying attention? Is It because you don’t have any idea how to earn money online? Or are you intimidated by the thought of it because you’re not tech-savvy?

Throw any negative thoughts out of your mind and let us help you build a $100,000 + yearly income that runs on automatic. We’re not promising a million dollars overnight or that you’ll be able to quit your job tomorrow, BUT if an extra $10,000 per month would help you reach your goals, then you should take action today!

OUR SIMPLE IS SO EASY TO USE, A FIFTH GRADER COULD BE SUCCESSFUL!

We’re so sure you will be successful with our system that we are inviting you to
GET STARTED TODAY FOR FREE!!!

That’s right…for FREE! No credit card is required.

GO SIGN UP NOW:
www.qmvhub.com/joinFREE
Enter Referral ID#

LK-R7859

Free offer expires in 48 hours!!!

Instructions for designers:
I’d like the color scheme to stay consistent with my company’s color scheme. To see the color scheme of Blue Harbor Gain go to www.qmvhub.com
As you are reading the text, please make certain parts of the text be emphasized on the postcard – wherever you feel necessary. When you read it, what would catch your attention? Those parts are the parts I’d like you to emphasize on the card by making them bolder, or a different color, or larger or highlighted.

The postcard is a 4x6 card, double-sided, full color

The text above is for the front side. The back will be the same thing, except in the spot where I have LK-R7859. On the backside it should say: (Use ID# on reverse side)

It’s like you are really only designing a one-sided card because the back side is almost an exact duplicate.

Thank you, you rock! =)

Target Market(s)

work from home seekers / make money online enthusiasts

Font styles to use
Serif

Requirements
Must have
• Color scheme similar to the color scheme at www.qmvhub.com
• The rest of the requirements are attached to the word doc.
• I will also send the logo, but it wouldn't let me upload because the file is too large.
Nice to have
• I really I am looking for something that really looks clean, but attention-grabbing

```html
<!DOCTYPE html>
<html lang="en">
<head>
<meta charset="utf-8">
<title>Blue Harbor Gain Postcard</title>
<link href="https://fonts.googleapis.com/css2?family=Lato:wght@400;700;900&family=PT+Sans:wght@400;700&family=Arimo:wght@400;700&display=swap" rel="stylesheet">
<style>
  :root {
    --stage: #747474;
    --card: #ffffff;
    --brand-blue: #5ab4d6;
    --brand-blue-deep: #2f8fbf;
    --brand-blue-light: #a8dcf0;
    --alert-red: #c8171e;
    --ink: #1a1a1a;
    --ink-soft: #3c3c3c;
  }
  * { box-sizing: border-box; margin: 0; padding: 0; }
  html, body { width: 1200px; height: 1200px; overflow: hidden; }
  body { background: var(--stage); position: relative; font-family: "Lato", sans-serif; color: var(--ink); }

  .postcard { position: absolute; background: var(--card); overflow: hidden; box-shadow: 0 2px 6px rgba(0,0,0,.35); }
  .postcard--front { left: 188px; top: 91px; width: 638px; height: 494px; }
  .postcard--back  { left: 425px; top: 606px; width: 639px; height: 495px; }

  /* front */
  .hero-visual { position: absolute; inset: 0; }
  .brand { position: absolute; left: 42px; top: 34px; }
  .brand__name { font-family: "Lato", sans-serif; font-weight: 900; font-size: 27px; color: var(--ink-soft); letter-spacing: -0.3px; }

  .salutation { position: absolute; left: 15px; top: 106px; font-weight: 700; font-size: 23px; color: var(--brand-blue); letter-spacing: -0.3px; }
  .salutation-rule { position: absolute; left: 15px; top: 137px; width: 238px; height: 2px; background: var(--brand-blue); }

  .letter { position: absolute; left: 15px; top: 152px; width: 300px; font-size: 14.4px; line-height: 17.5px; font-weight: 400; color: var(--ink); }
  .letter p + p { margin-top: 8px; }
  .letter strong { font-weight: 700; }

  .pointer-arrow { position: absolute; left: 214px; top: 240px; width: 34px; height: 46px; }

  .offer-pill { position: absolute; left: 17px; top: 293px; width: 298px; height: 110px; border-radius: 55px; background: var(--brand-blue); color: #fff; text-align: center; font-family: "Arimo", sans-serif; }
  .offer-pill__amount { display: block; font-weight: 700; font-size: 46px; line-height: 44px; margin-top: 4px; letter-spacing: 0.5px; }
  .offer-pill__line { display: block; font-size: 24.5px; line-height: 28px; letter-spacing: 0.4px; }
  .offer-pill__now { display: block; font-weight: 700; font-size: 26px; line-height: 30px; }

  .signup { position: absolute; text-align: center; font-family: "Arimo", sans-serif; }
  .signup__label { display: block; font-size: 17px; color: var(--ink); letter-spacing: 0.2px; }
  .signup__url { display: block; font-weight: 700; font-size: 20.5px; color: var(--brand-blue); margin-top: 5px; }
  .postcard--front .signup { left: 15px; width: 300px; top: 424px; }

  /* back */
  .copy-column { position: absolute; left: 0; top: 0; width: 310px; }
  .blue-band { background: var(--brand-blue); color: #fff; padding: 13px 16px 8px 16px; font-family: "PT Sans", sans-serif; font-size: 10.6px; line-height: 13.4px; text-align: justify; }
  .blue-band p + p { margin-top: 6px; }
  .blue-band--intro { height: 160px; }
  .tagline { padding: 5px 16px 0; height: 46px; font-family: "PT Sans", sans-serif; font-weight: 700; font-size: 13.6px; line-height: 18px; color: var(--brand-blue-deep); text-transform: uppercase; letter-spacing: 0.2px; }
  .blue-band--invite { height: 76px; padding-top: 9px; font-size: 11.6px; line-height: 15px; text-align: left; }
  .invite__cta { display: block; margin-top: 5px; font-size: 17.5px; line-height: 19px; color: var(--alert-red); text-transform: uppercase; }
  .invite__note { display: block; font-family: "Arimo", sans-serif; font-weight: 700; font-size: 10.4px; color: #fff; }

  .referral { position: absolute; left: 15px; top: 291px; width: 283px; height: 56px; border-top: 1px dashed var(--ink); border-bottom: 1px dashed var(--ink); padding: 4px 6px 0; }
  .referral__label { font-weight: 700; font-size: 21px; line-height: 24px; color: var(--ink); }
  .referral__expiry { font-weight: 900; font-size: 19.5px; line-height: 22px; color: var(--alert-red); }
  .postcard--back .signup { left: 15px; width: 283px; top: 362px; }
  .postcard--back .signup__url { font-size: 18.5px; }
</style>
</head>
<body>

  <section class="postcard postcard--front" aria-label="Postcard front">
    <svg class="hero-visual" viewBox="0 0 638 494">
      <defs>
        <linearGradient id="portraitTone" x1="0" y1="0" x2="1" y2="1">
          <stop offset="0" stop-color="#f1f1f1"/>
          <stop offset="0.5" stop-color="#d6d6d6"/>
          <stop offset="1" stop-color="#9c9fa6"/>
        </linearGradient>
      </defs>
      <path role="img" aria-label="Portrait of a confident businesswoman in a grey suit with arms crossed"
            d="M462 0 Q 330 120 340 260 Q 352 400 525 494 L 638 494 L 638 0 Z" fill="url(#portraitTone)"/>
      <path d="M448 0 Q 300 120 316 260 Q 332 410 512 494 L 528 494 Q 346 405 330 260 Q 318 125 462 0 Z" fill="var(--brand-blue-light)"/>
      <path d="M470 0 Q 332 125 340 262 Q 352 405 536 494 L 544 494 Q 360 402 348 262 Q 340 128 478 0 Z" fill="var(--brand-blue)"/>
    </svg>

    <div class="brand">
      <span class="brand__name">Blue Harbor Gain</span>
    </div>

    <h1 class="salutation">To My Dear Colleague,</h1>
    <div class="salutation-rule"></div>

    <div class="letter">
      <p>This week, I want you to do yourself and me a favor, okay?</p>
      <p><strong>I want you to ask your boss for a $100,000 per year salary increase.</strong> If the answer is no then I want you to “give yourself” a</p>
    </div>

    <svg class="pointer-arrow" viewBox="0 0 34 46" aria-hidden="true">
      <path d="M30 2 Q 32 22 14 36" fill="none" stroke="var(--alert-red)" stroke-width="1.6"/>
      <path d="M6 42 L 12 28 L 20 38 Z" fill="none" stroke="var(--alert-red)" stroke-width="1.6" stroke-linejoin="round"/>
    </svg>

    <div class="offer-pill">
      <span class="offer-pill__amount">$10,000</span>
      <span class="offer-pill__line">per month pay increase</span>
      <span class="offer-pill__now">RIGHT NOW!</span>
    </div>

    <div class="signup">
      <span class="signup__label">GO SIGN UP NOW:</span>
      <span class="signup__url">www.qmvhub.com/joinFREE</span>
    </div>
  </section>

  <section class="postcard postcard--back" aria-label="Postcard back">
    <div class="copy-column">
      <div class="blue-band blue-band--intro">
        <p>The opportunity to make 6-7 figures using SIMPLE online systems is exploding right before your eyes. Why aren’t you paying attention? Is It because you don’t have any idea how to earn money online? Or are you intimidated by the thought of it because you’re not tech-savvy?</p>
        <p>Let us help you build a $100,000 + yearly income that runs on automatic. We’re not promising a million dollars overnight or that you’ll be able to quit your job tomorrow, BUT if an extra $10,000 per month would help you reach your goals, then you should take action today!</p>
      </div>
      <p class="tagline">Our simple is so easy to use, a fifth grader could be successful!</p>
      <div class="blue-band blue-band--invite">
        We’re so sure you will be successful with our system that we are inviting you to
        <span class="invite__cta">Get started today for free!!!</span>
        <span class="invite__note">That’s right…for FREE! No credit card is required.</span>
      </div>
    </div>

    <div class="referral">
      <p class="referral__label">Enter Referral ID</p>
      <p class="referral__expiry">Free offer expires in 48 hours!!!</p>
    </div>

    <div class="signup">
      <span class="signup__label">GO SIGN UP NOW:</span>
      <span class="signup__url">www.qmvhub.com/joinFREE</span>
    </div>
  </section>

</body>
</html>
```